Web Design for UK Based Technology Company*

Korvane is a new entrant in the data marketplace.
It is offering two direct API services to help clients access:
- Company Data
- Location Data
We also offer data services and consulting to help companies to integrate our API services and the data derived from them into their businesses. Our aim is to offer both the technology and services to help businesses use and integrate data better. It is a modern business built to support a modern world.

Target Market(s)

Business Professionals and decision makers

Industry/Entity Type

It Service

Number of Pages Required

5+ page

Font styles to use
Sans Serif

Colors

Designer to choose colors to be used in the design.

Requirements
Must have
• The full suite of PSD designs taking into account the layouts and wireframes supplied with which it will be compared. Focus on the homepage first. It has to have a consistent theme/feel. It has to fit with the logo.
Nice to have
• Simple, clean, a few strong ideas.
Should not have
• Cartoons, overdesign, loud colours.

```html
<!DOCTYPE html>
<html lang="en">
<head>
<meta charset="utf-8">
<title>Korvane – Richer Data to Drive Your Business</title>
<link href="https://fonts.googleapis.com/css2?family=Open+Sans:wght@400;600;700&display=swap" rel="stylesheet">
<style>
:root{
  --brand:#1a6fab;
  --brand-dark:#145a8c;
  --brand-deep:#0f4a77;
  --sky:#62b7e6;
  --sky-light:#8fd0f2;
  --ink:#222;
  --muted:#555;
  --line:#d6dde4;
  --pale:#eef3f8;
  --white:#fff;
}
*{box-sizing:border-box;margin:0;padding:0}
html,body{width:1200px;height:3568px;overflow:hidden}
body{font-family:"Open Sans",Arial,sans-serif;color:var(--ink);background:var(--white);position:relative}
a{color:inherit;text-decoration:none}
.abs{position:absolute}
.btn{display:inline-flex;align-items:center;gap:8px;height:34px;padding:0 14px;font-size:13px;font-weight:600;border:2px solid var(--brand);color:var(--brand);background:var(--white);border-radius:3px;text-transform:uppercase;white-space:nowrap}
.btn-solid{background:var(--brand);color:var(--white)}
.btn-light{border-color:var(--white);color:var(--white);background:transparent}
.btn svg{width:15px;height:15px}

/* header */
.site-header{top:0;left:0;width:1200px;height:104px;background:var(--white)}
.brand{left:119px;top:30px;display:flex;align-items:center;gap:10px;font-size:28px;font-weight:600;color:var(--brand-deep);letter-spacing:1px}
.brand-dot{width:30px;height:30px;border-radius:50%;background:var(--brand)}
.header-call{left:676px;top:22px;font-size:11px;color:var(--muted)}
.header-call b{font-size:15px;color:var(--brand-deep)}
.header-login{left:873px;top:15px;height:32px}
.header-trial{left:982px;top:15px;height:32px}
.main-nav{top:72px;right:120px;display:flex;font-size:11px;font-weight:600;color:#333}
.main-nav a{padding:0 26px;border-left:1px solid #bbb;line-height:14px}
.main-nav a:first-child{border-left:0}
.main-nav a:last-child{padding-right:0}

/* hero */
.hero{top:104px;left:0;width:1200px;height:489px;background:linear-gradient(180deg,var(--sky) 0%,#6fc0ea 100%)}
.hero-title{left:119px;top:138px;font-size:46px;line-height:63px;font-weight:700;color:var(--white);letter-spacing:1px}
.hero-dots{left:119px;top:346px;display:flex;gap:7px}
.hero-dots i{width:10px;height:10px;border-radius:50%;border:1.5px solid var(--white)}
.hero-dots i:first-child{background:var(--white)}
.hero-art{left:554px;top:96px;width:607px;height:272px;border-radius:120px 120px 40px 40px;background:radial-gradient(ellipse at 50% 60%,#a9dcf5 0%,#86cbef 55%,rgba(111,192,234,0) 80%)}
.feature-card{top:532px;width:495px;height:128px;background:var(--brand);border-radius:4px;display:flex;align-items:center;justify-content:space-between;padding:0 32px 0 30px;box-shadow:0 6px 14px rgba(0,0,0,.12)}
.feature-card h2{font-size:22px;line-height:32px;font-weight:600;color:var(--white);text-transform:uppercase}
.card-company{left:97px}
.card-location{left:607px}

/* intro */
.intro{top:730px;left:160px;width:880px;text-align:center;font-size:12px;line-height:21px;color:var(--muted)}
.intro p{margin-bottom:11px}

/* products */
.product-img{height:375px}
.img-company{left:119px;top:992px;width:642px;background:linear-gradient(135deg,#2c3540 0%,#5a6b7c 45%,#9aa8b4 70%,#3d4650 100%)}
.img-location{left:439px;top:1443px;width:641px;background:linear-gradient(135deg,#1d3f9a 0%,#4368c2 50%,#b4c2ea 100%)}
.price-badge{width:114px;height:114px;border-radius:50%;border:1.5px solid #9cc3df;display:flex;flex-direction:column;align-items:center;justify-content:center;color:var(--brand)}
.price-badge small{font-size:13px}
.price-badge strong{font-size:25px;line-height:28px;color:var(--brand-deep)}
.product-title{font-size:30px;font-weight:400;color:#111}
.product-text{font-size:16.5px;line-height:25px;color:var(--muted)}
.btn-row{display:flex;gap:9px}

/* go ahead */
.go-ahead{top:1931px;left:0;width:1200px;height:395px;background:linear-gradient(180deg,#f1f5f9 0%,#e8eef4 100%);text-align:center}
.go-ahead h2{position:absolute;top:62px;width:100%;font-size:41px;font-weight:700;color:var(--brand-deep);letter-spacing:1px}
.go-ahead h3{position:absolute;top:130px;width:100%;font-size:32px;font-weight:400;color:#111}
.go-ahead p{position:absolute;top:198px;left:130px;width:940px;font-size:16.5px;line-height:30px;color:var(--muted)}
.go-ahead p u{color:#333}
.go-ahead .btn-row{position:absolute;top:283px;left:0;width:100%;justify-content:center;gap:12px}

/* demanding */
.demanding{top:2326px;left:0;width:1200px;height:492px;background:var(--brand-dark)}
.team-photo{left:120px;top:2402px;width:416px;height:491px;border:4px solid var(--white);outline:2px solid var(--brand);background:linear-gradient(160deg,#d9d2c8 0%,#8a7262 35%,#c7c2bd 65%,#eceae8 100%);z-index:2}
.demanding-body{left:577px;top:2405px;width:520px;color:var(--white)}
.demanding-body h2{font-size:28px;line-height:40px;font-weight:600;text-transform:uppercase}
.demanding-body .lead{margin-top:24px;font-size:12px;line-height:18px}
.demanding-body ul{list-style:none;margin-top:8px}
.demanding-body li{font-size:12px;font-weight:600;line-height:28px;padding-left:14px;position:relative}
.demanding-body li::before{content:"›";position:absolute;left:0;font-size:16px}
.demanding-body .closing{margin-top:4px;font-size:12.5px;font-weight:600}
.cta-pair{left:577px;top:2708px;display:flex;align-items:center}
.cta-pair .btn{height:36px}
.or-mark{width:38px;height:38px;margin:0 -6px;border-radius:50%;background:var(--white);color:var(--brand);font-size:11px;font-weight:700;display:flex;align-items:center;justify-content:center;border:3px solid var(--brand-dark);z-index:1}

/* map */
.map-area{top:2818px;left:0;width:1200px;height:450px;background:linear-gradient(90deg,#e9ecef 0%,#f1f3f5 50%,#e6e9ec 100%)}
.address-card{left:396px;top:2983px;width:390px;height:205px;background:var(--white);border:1px solid var(--line);box-shadow:0 4px 14px rgba(0,0,0,.08);padding:36px 36px 0 38px;z-index:2}
.address-line{display:flex;gap:14px;font-size:14.5px;line-height:20px;color:#222}
.address-line svg{flex:none;width:18px;height:22px;margin-top:2px}
.address-phone{display:flex;align-items:center;gap:10px;margin-top:16px;font-size:22px;color:var(--brand)}
.address-card .btn{margin-top:14px}

/* footer */
.site-footer{top:3268px;left:0;width:1200px;height:300px;background:var(--white)}
.footer-col{top:79px}
.footer-col h4{font-size:16px;font-weight:600;color:var(--brand);text-transform:uppercase;margin-bottom:8px}
.footer-col a{display:block;font-size:12px;line-height:24px;color:#555}
.footer-col a::before{content:"›";margin-right:6px}
.footer-brand{left:884px;top:116px;display:flex;align-items:center;gap:10px;font-size:32px;font-weight:600;color:#111;white-space:nowrap}
.footer-brand span{width:32px;height:32px;background:var(--brand);border-radius:50%;flex:none}
.footer-rule{left:119px;top:252px;width:961px;height:1px;background:var(--line)}
.copyright{left:119px;top:270px;font-size:11px;color:#555}
.legal{right:120px;top:270px;font-size:11px;color:#555;display:flex}
.legal a{padding:0 12px;border-left:1px solid #aaa;line-height:12px}
.legal a:first-child{border-left:0}
.legal a:last-child{padding-right:0}
</style>
</head>
<body>

<header class="site-header abs">
  <a class="brand abs" href="#"><span class="brand-dot"></span>KORVANE</a>
  <div class="header-call abs">CALL US ON : <b>(019) 496 - 073</b></div>
  <a class="btn header-login abs" href="#"><svg viewBox="0 0 16 16" fill="none" stroke="currentColor" stroke-width="1.6"><path d="M9 2h5v12H9M2 8h8M7 5l3 3-3 3"/></svg>Login</a>
  <a class="btn btn-solid header-trial abs" href="#">Free Trial</a>
  <nav class="main-nav abs">
    <a href="#">COMPANY DATA</a><a href="#">LOCATION DATA</a><a href="#">SERVICES</a><a href="#">ABOUT US</a><a href="#">CONTACT US</a>
  </nav>
</header>

<section class="hero abs">
  <h1 class="hero-title abs">RICHER DATA<br>TO DRIVE YOUR<br>BUSINESS</h1>
  <div class="hero-dots abs"><i></i><i></i><i></i></div>
  <div class="hero-art abs" role="img" aria-label="Illustration of cloud-connected devices sharing secure data"></div>
</section>

<div class="feature-card card-company abs">
  <h2>Comprehensive<br>Company Information</h2>
  <a class="btn btn-light" href="#">Company API</a>
</div>
<div class="feature-card card-location abs">
  <h2>Bring Mapping Data<br>Into Your Business</h2>
  <a class="btn btn-light" href="#">Location API</a>
</div>

<section class="intro abs">
  <p>Korvane is setup for connected world. A world where data is integrated, comprehensive and useful. Where systems are designed to cooperate to make businesses more efficient. For this purpose we have focused on two key areas of work - location and company data.</p>
  <p>Our Postcode API is the most current in the marketplace, helping anyone pinpoint a map simply by providing a postcode. This allows you to assign a location to your postcode-level business data. We also provide an Address API, giving you an address for any postcode along with it's coordinate on the ground. We also supply base maps for customers looking to use maps on their website. And we supply a wide range of bespoke GIS services for more specific mapping work.</p>
  <p>For company data we have restructured the Company Registry data into something more useful and practical for businesses. Just supply one or more company numbers and we can send you back detailed company information covering a raft of data. Better still this data can be supplied either as a file or by API so you can receive it in the format you prefer.</p>
</section>

<div class="product-img img-company abs" role="img" aria-label="Photo of a hand holding a phone surrounded by connected network icons"></div>
<div class="price-badge abs" style="left:805px;top:1021px"><small>FROM ONLY</small><strong>£29 PM</strong></div>
<h2 class="product-title abs" style="left:805px;top:1162px">COMPANY API</h2>
<p class="product-text abs" style="left:805px;top:1213px;width:290px">You supply one or more company numbers - We send back everything via a simple API or CSV file</p>
<div class="btn-row abs" style="left:805px;top:1303px"><a class="btn btn-solid" href="#">Free Trial</a><a class="btn" href="#">Find Out More</a></div>

<div class="price-badge abs" style="left:289px;top:1459px"><small>FROM ONLY</small><strong>£29 PM</strong></div>
<h2 class="product-title abs" style="right:797px;top:1600px">LOCATION API</h2>
<p class="product-text abs" style="right:797px;top:1650px;width:300px;text-align:right">You send us a postcode we send you the location. Or you send us the location, we send back the postcode : API or CSV.</p>
<div class="btn-row abs" style="right:797px;top:1766px"><a class="btn btn-solid" href="#">Free Trial</a><a class="btn" href="#">Find Out More</a></div>
<div class="product-img img-location abs" role="img" aria-label="Photo of a world map overlay with location markers above a tablet"></div>

<section class="go-ahead abs">
  <h2>GO AHED :</h2>
  <h3>TEST OUR DATA, OR LET’S TALK IT THROUGH...</h3>
  <p>If you are confident you know what you want, why not <u>start a trial</u> ? It’s free of charge and you can test the service for a limited time. If you are not so sure or you have a very specific requirements then talk to our consultants.</p>
  <div class="btn-row">
    <a class="btn" href="#"><svg viewBox="0 0 16 16" fill="none" stroke="currentColor" stroke-width="1.4"><path d="M4 1.5l2.5 3-1.5 2a8 8 0 004.5 4.5l2-1.5 3 2.5-1.5 2.5C7 14.5 1.5 9 1.5 3z"/></svg>Call : (019) 496 - 073</a>
    <a class="btn" href="#"><svg viewBox="0 0 16 16" fill="none" stroke="currentColor" stroke-width="1.4"><rect x="1.5" y="3.5" width="13" height="9"/><path d="M1.5 3.5L8 9l6.5-5.5"/></svg>Send an Email</a>
  </div>
</section>

<section class="demanding abs"></section>
<div class="team-photo abs" role="img" aria-label="Photo of three colleagues reviewing documents at a laptop"></div>
<div class="demanding-body abs">
  <h2>Demanding Data Requirements?<br>Look Further</h2>
  <p class="lead">Most business looking for our help have coplex data requirements they need to piece togerther. It may be they have an in-house team, but if not, we can help with :</p>
  <ul>
    <li>Connecting our API into existing systems and software</li>
    <li>Helping with more complex business or location data supply</li>
    <li>Placing experienced staff on site to assist with mapping and data projects</li>
    <li>Helping business automate and digitally transform</li>
  </ul>
  <p class="closing">So if you want us to help you take your integrations up a notch, then let’s talk.</p>
</div>
<div class="cta-pair abs">
  <a class="btn btn-light" href="#"><svg viewBox="0 0 16 16" fill="none" stroke="currentColor" stroke-width="1.4"><path d="M4 1.5l2.5 3-1.5 2a8 8 0 004.5 4.5l2-1.5 3 2.5-1.5 2.5C7 14.5 1.5 9 1.5 3z"/></svg>Call : (019) 496 - 073</a>
  <span class="or-mark">OR</span>
  <a class="btn btn-light" href="#" style="padding-left:20px">Bespoke Services</a>
</div>

<section class="map-area abs" role="img" aria-label="Street map showing the office location"></section>
<div class="address-card abs">
  <div class="address-line">
    <svg viewBox="0 0 18 22" fill="none" stroke="#1a6fab" stroke-width="1.4"><path d="M9 21s7-7.5 7-12.5A7 7 0 002 8.5C2 13.5 9 21 9 21z"/><circle cx="9" cy="8.5" r="2.5"/></svg>
    <span>Unit 4, Harrowgate Yard, Linmoor Park, Eastbrook, Readwell RW4 2KP</span>
  </div>
  <div class="address-phone"><svg viewBox="0 0 16 16" width="20" height="20" fill="none" stroke="currentColor" stroke-width="1.2"><path d="M4 1.5l2.5 3-1.5 2a8 8 0 004.5 4.5l2-1.5 3 2.5-1.5 2.5C7 14.5 1.5 9 1.5 3z"/></svg>(019) 496 - 073</div>
  <a class="btn" href="#"><svg viewBox="0 0 16 16" fill="none" stroke="currentColor" stroke-width="1.4"><rect x="1.5" y="3.5" width="13" height="9"/><path d="M1.5 3.5L8 9l6.5-5.5"/></svg>Send an Email</a>
</div>

<footer class="site-footer abs">
  <div class="footer-col abs" style="left:119px"><h4>Company Data</h4><a href="#">Company Information</a><a href="#">Alerts and Notifications</a><a href="#">Contact Information</a><a href="#">Financial Information</a><a href="#">Other Data Services</a></div>
  <div class="footer-col abs" style="left:334px"><h4>Location Data</h4><a href="#">Postcode Lookup</a><a href="#">Address Lookup</a><a href="#">Base Mapping</a><a href="#">Boundaries</a><a href="#">Bespoke Mapping</a></div>
  <div class="footer-col abs" style="left:535px"><h4>Services</h4><a href="#">API / Integrations</a><a href="#">Licensing / IPR</a><a href="#">Complex Location Data</a><a href="#">Digital Transformation</a></div>
  <div class="footer-col abs" style="left:748px"><h4>Korvane</h4><a href="#">Pricing</a><a href="#">About Us</a><a href="#">Contact Us</a><a href="#">Free Trial</a><a href="#">Login</a></div>
  <div class="footer-brand abs"><span></span>KORVANE</div>
  <div class="footer-rule abs"></div>
  <div class="copyright abs">(c) Brightfold Studio Limited. All rights reserved</div>
  <nav class="legal abs"><a href="#">Sitemap</a><a href="#">Terms of Use</a><a href="#">Privacy Policy</a><a href="#">Contact Us</a></nav>
</footer>

</body>
</html>
```